Buch-/eBook-Cover für Geschichte zum Pride auf Gran Canaria
Zielgruppe
Zielgruppe: Reisefreudige junge schwule Männer
Aufgabenstellung
Die Geschichte spielt zum Pride auf Gran Canaria. Es geht um vier Freunde die dort ihre Ferien verbingen.
Ich stelle mir vor, dass auf dem Cover die Regenbogenflagge ist, Strand, Meer, keine Menschen und ein fetter Schriftzug mit dem Titel #LuvaronaSommer. Daneben sollte kleiner mein Name Torben van Hulsdorf stehen. Das Cover kann aber auch gern wie ein Partyflyer designt sein und der Titel wie ein Logo wirken.
Bin aber für alternativen offen.

```html
<!DOCTYPE html>
<html lang="de">
<head>
<meta charset="utf-8">
<title>#LuvaronaSommer – Torben van Hulsdorf</title>
<link rel="stylesheet" href="https://fonts.googleapis.com/css2?family=Fraunces:opsz,wght@9..144,700;9..144,800&display=swap">
<style>
  :root {
    --ink: #37220f;
    --sky-cream: #fbf7ea;
    --sky-haze: #d9eef4;
    --sea: #2db4df;
    --sea-deep: #1f93c4;
    --sand-light: #d8b27a;
    --sand: #c49258;
    --sand-dark: #9a6b3a;
    --rb-red: #f0435a;
    --rb-orange: #f7a325;
    --rb-yellow: #f8d531;
    --rb-green: #35b457;
    --rb-blue: #2f8fd6;
    --rb-violet: #6a2a8f;
  }
  html, body {
    margin: 0;
    padding: 0;
    width: 848px;
    height: 1200px;
    overflow: hidden;
    background: #ffffff;
  }
  .cover {
    position: relative;
    width: 848px;
    height: 1200px;
    overflow: hidden;
    font-family: "Fraunces", Georgia, serif;
    color: var(--ink);
  }
  .cover__scene {
    position: absolute;
    inset: 0;
    background: linear-gradient(
      to bottom,
      var(--sky-cream) 0%,
      var(--sky-cream) 36%,
      var(--sky-haze) 50%,
      #9fd8ec 56%,
      var(--sea) 59%,
      var(--sea-deep) 62%,
      var(--sand-dark) 64%,
      var(--sand-light) 70%,
      var(--sand) 85%,
      var(--sand-dark) 100%
    );
  }
  .cover__flag {
    position: absolute;
    inset: 0;
    width: 848px;
    height: 1200px;
  }
  .cover__text {
    position: absolute;
    top: 96px;
    right: 92px;
    text-align: right;
  }
  .cover__author {
    margin: 0 0 30px;
    font-size: 19px;
    font-weight: 700;
    letter-spacing: 0.2px;
    padding-right: 6px;
  }
  .cover__title {
    margin: 0;
    font-size: 126px;
    font-weight: 800;
    line-height: 121px;
    letter-spacing: -1px;
  }
  .cover__title span {
    display: block;
  }
</style>
</head>
<body>
  <main class="cover">
    <div class="cover__scene" role="img" aria-label="Gemalte Dünenlandschaft mit Strand, Meer und hellem Himmel"></div>

    <svg class="cover__flag" viewBox="0 0 848 1200" role="img" aria-label="Gemalte, wehende Regenbogenflagge in Wellenlinien am linken Rand">
      <defs>
        <linearGradient id="rainbow" x1="0" y1="0" x2="1" y2="1">
          <stop offset="0" stop-color="var(--rb-violet)"/>
          <stop offset="0.2" stop-color="var(--rb-blue)"/>
          <stop offset="0.4" stop-color="var(--rb-green)"/>
          <stop offset="0.6" stop-color="var(--rb-yellow)"/>
          <stop offset="0.8" stop-color="var(--rb-orange)"/>
          <stop offset="1" stop-color="var(--rb-red)"/>
        </linearGradient>
      </defs>
      <path fill="url(#rainbow)" opacity="0.92"
            d="M0 0 H250 C270 40 275 80 262 120 C245 170 200 210 150 250 C100 290 40 330 0 360 Z"/>
      <path fill="url(#rainbow)" opacity="0.92"
            d="M0 500 C70 520 140 560 190 620 C220 660 225 720 230 780 C240 880 300 950 400 980 C520 1010 650 990 848 960 V1200 H0 Z"/>
    </svg>

    <header class="cover__text">
      <p class="cover__author">Torben van Hulsdorf</p>
      <h1 class="cover__title">
        <span>#Luva</span>
        <span>rona</span>
        <span>Som</span>
        <span>mer</span>
      </h1>
    </header>
  </main>
</body>
</html>
```